依頼詳細
■求めている人材
女性(25才~30才:独身)
正社員

■サイトマップ
①トップ
②新卒採用
⓷中途採用
④代表メッセージ
⑤会社概要・沿革
⑥社員の声
⑦充実した福利厚生
⑧トピックス(注目している内容)
⑨ニュース
⑩当サロンについて
⑪募集要項
⑫入社方法
⑬パート
⑭教育システム
⑮サロン見学・お問い合わせ

■情報元
オフィシャルサイト:http://www.mireno.bz/
求人媒体:https://kotori-work.com/job/048315#job__shop-detail
※上記サイトから引用して頂いて問題ありません。

■参考サイト
http://hairstyle-novalu.com/recruit/(サイトマップも参考にしています)

■テイスト・色味
日常感とモード間をMIXにしたイメージが好きです。(女性向き)
赤色 / 黄色・オレンジ / 茶系

■素材について
①サロン(内観・コンテンスト写真等)
枚数が多いため、下記URLよりダウンロードください。
http://25.filebako.nu/0715-a9f3e1d07c62b4e8d1f02a7b59c3e6d18

②その他
ピクセラ(https://jp.pixelima.com/)と契約しておりますので、
定期契約内の写真であれば
素材として用いて頂けます。選定後正規画像をお渡ししますので
提案時は仮画像にて配置ください。
ページ数
1ページ
希望イメージ
シンプル 複雑
単色 カラフル
暗い 明るい
日常 高級
遊び心 厳粛
未来的 伝統的
女性的 男性的
希望する色
赤系、茶系、黄・オレンジ系
納品ファイル
• 高解像度JPG (.jpg)
• イラストレーター形式 (.ai)
• フォトショップ形式 (.psd)
• PNG形式 (.png)
この度はお世話になっております。
提案数が芳しくない為、こちら都合で大変申し訳ありませんが
1週間延長させていただきます。
再度延長致します。
素材データのURLの保存期限が切れてしまったため
再度上げなおしました。
http://28.filebako.nu/0804-e7d1a93b50c4f82e6b19d3a07f5c2b8ad

色味のバランスや見せ方がとても良いと思いました。

ご提案頂きましてありがとうございました。
またこのような機会がありましたら、是非とも宜しくお願い致します。

```html
<!DOCTYPE html>
<html lang="ja">
<head>
<meta charset="utf-8">
<title>LUMERA HAIR 採用サイト</title>
<link href="https://fonts.googleapis.com/css2?family=Noto+Sans+JP:wght@300;400;500;700&family=Montserrat:wght@400;500;600&display=swap" rel="stylesheet">
<style>
:root{
  --orange:#f29a2e;
  --ink:#333333;
  --ink-soft:#666666;
  --line:#cfcfcf;
  --paper:#ffffff;
  --mist:#f3f3f3;
  --stone:#e4e4e4;
  --footer:#3a3a3a;
}
*{box-sizing:border-box;margin:0;padding:0}
html,body{width:1200px;height:4508px;overflow:hidden}
body{position:relative;background:var(--paper);font-family:"Noto Sans JP",sans-serif;color:var(--ink)}
.abs{position:absolute}
.photo{position:absolute}
.band{position:absolute;background:var(--mist)}
.band.dark{background:var(--stone)}
.card{position:absolute;background:var(--paper);box-shadow:0 2px 14px rgba(0,0,0,.05)}
.heading{text-align:center;font-family:"Montserrat","Noto Sans JP",sans-serif;font-weight:500;font-size:22px;letter-spacing:.08em}
.heading small{display:block;font-family:"Noto Sans JP",sans-serif;font-size:11px;font-weight:400;color:var(--ink-soft);letter-spacing:.1em;margin-top:2px}
.heading::after{content:"";display:block;width:40px;height:3px;background:var(--orange);margin:10px auto 0}
.heading.left{text-align:left}
.heading.left::after{margin-left:0}
.lead{font-size:20px;line-height:1.7;letter-spacing:.06em}
.body-text{font-size:13px;line-height:2;color:var(--ink-soft);letter-spacing:.04em}
.more{display:flex;align-items:center;gap:10px;font-family:"Montserrat",sans-serif;font-size:12px;color:var(--orange);letter-spacing:.06em}
.more svg{display:block}
.menu{left:36px;top:40px;display:flex;align-items:center;gap:14px;font-family:"Montserrat",sans-serif;font-size:15px;letter-spacing:.1em}
.brand{left:0;width:1200px;top:34px;text-align:center;font-weight:700;font-size:34px;letter-spacing:.02em}
.cta{right:0;top:0;width:208px;height:100px;background:var(--orange);color:#fff;font-size:14px;font-weight:500;line-height:1.6;display:flex;flex-direction:column;align-items:center;justify-content:center;text-align:center}
.label{position:absolute;background:#fff;padding:12px 0 0 20px}
.label-title{font-family:"Montserrat",sans-serif;font-weight:600;font-size:17px;letter-spacing:.04em;white-space:nowrap}
.label-sub{font-size:11px;color:var(--ink-soft)}
.label-bar{width:34px;height:3px;background:var(--orange);margin-top:8px}
.news-row{font-size:13px;color:var(--ink-soft);line-height:1.6}
.news-row time{color:var(--orange);font-family:"Montserrat",sans-serif;font-size:12px}
.hours{font-size:14px;line-height:1.8}
.detail-btn{border:1px solid var(--ink-soft);display:flex;align-items:center;justify-content:center;gap:14px;font-size:14px;background:rgba(255,255,255,.7)}
.site-footer{left:0;top:4312px;width:1200px;height:196px;background:var(--footer);color:#fff}
.social{display:flex;gap:18px;justify-content:center;padding-top:46px}
.social span{width:32px;height:32px;border-radius:50%;border:1px solid #ddd;display:block}
.foot-nav{display:flex;justify-content:center;margin-top:30px;font-size:13px}
.foot-nav span{padding:0 18px;border-left:1px solid #888}
.foot-nav span:first-child{border-left:none}
.copyright{text-align:center;font-family:"Montserrat",sans-serif;font-size:10px;color:#aaa;margin-top:26px;letter-spacing:.06em}
</style>
</head>
<body>

<header>
  <div class="abs menu">
    <svg width="34" height="18" viewBox="0 0 34 18"><g stroke="#333" stroke-width="2"><line x1="0" y1="1" x2="34" y2="1"/><line x1="0" y1="9" x2="34" y2="9"/><line x1="0" y1="17" x2="34" y2="17"/></g></svg>
    MENU
  </div>
  <div class="abs brand">LUMERA HAIR</div>
  <div class="abs cta">サロン見学<br>お問い合わせ
    <svg width="10" height="10" viewBox="0 0 10 10" style="margin-top:4px"><polyline points="2,1 7,5 2,9" fill="none" stroke="#fff" stroke-width="1.5"/></svg>
  </div>
</header>

<section class="recruit">
  <div class="band" style="left:0;top:100px;width:560px;height:460px"></div>
  <div class="photo" role="img" aria-label="笑顔の女性スタイリストの写真" style="left:560px;top:160px;width:640px;height:380px;background:linear-gradient(135deg,#d9cbbd,#b89a82 55%,#7a6658)"></div>
  <div class="card" style="left:48px;top:220px;width:552px;height:260px;padding:36px 40px">
    <div class="heading">RECRUIT<small>採用情報</small></div>
    <p class="body-text" style="margin-top:22px">文章が入ります。文章が入ります。文章が入ります。文章が入ります。<br>文章が入ります。文章が入ります。文章が入ります。文章が入ります。<br>文章が入ります。文章が入ります。文章が入ります。文章が入ります。<br>文章が入ります。文章が入ります。文章が入ります。</p>
  </div>
</section>

<section class="careers">
  <div class="photo" role="img" aria-label="新卒スタイリストの写真" style="left:152px;top:640px;width:232px;height:230px;background:linear-gradient(135deg,#a8958a,#5f4f47)"></div>
  <div class="label" style="left:272px;top:808px;width:220px">
    <div class="label-title">NEW GRADUATES</div>
    <div class="label-sub">新卒採用</div>
    <div class="label-bar"></div>
  </div>
  <div class="abs more" style="left:292px;top:882px">READ MORE <svg width="34" height="8" viewBox="0 0 34 8"><polyline points="0,7 33,7 26,1" fill="none" stroke="#f29a2e" stroke-width="1.2"/></svg></div>

  <div class="photo" role="img" aria-label="中途採用スタイリストの写真" style="left:624px;top:640px;width:232px;height:230px;background:linear-gradient(135deg,#c7b9ae,#7f6f63 60%,#596b4e)"></div>
  <div class="label" style="left:744px;top:808px;width:300px">
    <div class="label-title">MID-CAREER RECRUITING</div>
    <div class="label-sub">中途採用</div>
    <div class="label-bar"></div>
  </div>
  <div class="abs more" style="left:764px;top:882px">READ MORE <svg width="34" height="8" viewBox="0 0 34 8"><polyline points="0,7 33,7 26,1" fill="none" stroke="#f29a2e" stroke-width="1.2"/></svg></div>
</section>

<section class="message">
  <div class="band dark" style="left:0;top:910px;width:1200px;height:610px;z-index:-1"></div>
  <div class="band" style="left:328px;top:910px;width:872px;height:610px;z-index:-1"></div>
  <div class="photo" role="img" aria-label="代表者の写真" style="left:48px;top:980px;width:424px;height:452px;background:linear-gradient(160deg,#bba48a,#7d6551 60%,#3e342d)"></div>
  <div class="card" style="left:400px;top:1048px;width:672px;height:412px;padding:40px 60px 0 110px">
    <div class="heading">MESSAGE<small>代表メッセージ</small></div>
    <p class="lead" style="margin-top:26px">文章が入ります。文章が入ります。文章が入ります。<br>文章が入ります。文章が入ります。文章が入ります。</p>
    <p class="body-text" style="margin-top:12px">文章が入ります。文章が入ります。文章が入ります。文章が入ります。<br>文章が入ります。文章が入ります。文章が入ります。文章が入ります。<br>文章が入ります。文章が入ります。文章が入ります。文章が入ります。<br>文章が入ります。文章が入ります。文章が入ります。</p>
    <div class="more" style="margin-top:14px">READ MORE <svg width="34" height="8" viewBox="0 0 34 8"><polyline points="0,7 33,7 26,1" fill="none" stroke="#f29a2e" stroke-width="1.2"/></svg></div>
  </div>
</section>

<section class="staff-voice">
  <div class="band" style="left:0;top:1520px;width:330px;height:580px"></div>
  <div class="band dark" style="left:0;top:2100px;width:330px;height:80px"></div>
  <div class="card" style="left:180px;top:1592px;width:640px;height:448px;padding:44px 40px 0 32px">
    <div class="heading">STAFF VOICE<small>社員の声</small></div>
    <p class="lead" style="margin-top:26px">文章が入ります。文章が入ります。<br>文章が入ります。文章が入ります。文章が入ります。</p>
    <p class="body-text" style="margin-top:12px">文章が入ります。文章が入ります。文章が入ります。文章が入ります。<br>文章が入ります。文章が入ります。文章が入ります。文章が入ります。<br>文章が入ります。文章が入ります。文章が入ります。文章が入ります。<br>文章が入ります。文章が入ります。文章が入ります。</p>
    <div class="more" style="margin-top:14px">READ MORE <svg width="34" height="8" viewBox="0 0 34 8"><polyline points="0,7 33,7 26,1" fill="none" stroke="#f29a2e" stroke-width="1.2"/></svg></div>
  </div>
  <div class="photo" role="img" aria-label="男性スタッフの写真" style="left:720px;top:1560px;width:380px;height:500px;background:linear-gradient(160deg,#b9aa9c,#6e6158 55%,#2e2a28)"></div>
</section>

<section class="welfare">
  <div class="band" style="left:0;top:2180px;width:1200px;height:500px"></div>
  <div class="card" style="left:152px;top:2208px;width:896px;height:452px;padding:40px 0 0 0">
    <div class="heading">WELFARE<small>福利厚生</small></div>
  </div>
  <div class="photo" role="img" aria-label="サロン店内の写真" style="left:240px;top:2340px;width:340px;height:220px;background:linear-gradient(135deg,#8a6e52,#c99a62 45%,#3d3b3a)"></div>
  <div class="abs" style="left:612px;top:2348px">
    <p class="lead">文章が入ります。文章が入ります。</p>
    <p class="body-text" style="margin-top:10px">文章が入ります。文章が入ります。文章が入ります。<br>文章が入ります。文章が入ります。文章が入ります。<br>文章が入ります。文章が入ります。文章が入ります。<br>文章が入ります。文章が入ります。</p>
    <div class="more" style="margin-top:14px">READ MORE <svg width="34" height="8" viewBox="0 0 34 8"><polyline points="0,7 33,7 26,1" fill="none" stroke="#f29a2e" stroke-width="1.2"/></svg></div>
  </div>
</section>

<section class="topics">
  <div class="band dark" style="left:0;top:2680px;width:1200px;height:760px"></div>
  <div class="band" style="left:328px;top:2680px;width:872px;height:760px"></div>
  <div class="card" style="left:152px;top:2780px;width:896px;height:520px;padding:34px 0 0 0">
    <div class="heading">TOPICS<small>トピックス</small></div>
  </div>
  <div class="photo" role="img" aria-label="コンテスト受賞者の写真" style="left:152px;top:2920px;width:296px;height:200px;background:linear-gradient(135deg,#cfc6bd,#8c7f74)"></div>
  <div class="photo" role="img" aria-label="ステージ発表の写真" style="left:452px;top:2920px;width:296px;height:200px;background:linear-gradient(135deg,#6d5c52,#2a2626 70%)"></div>
  <div class="photo" role="img" aria-label="イベント会場の写真" style="left:752px;top:2920px;width:296px;height:200px;background:linear-gradient(135deg,#a49888,#d3b470 50%,#4c4540)"></div>
  <div class="abs" style="left:196px;top:3150px;width:230px">
    <p class="body-text" style="font-size:12px">文章が入ります。文章が入ります。<br><br>文章が入ります。文章が入ります。<br>文章が入ります。文章が入ります。<br>文章が入ります。文章が入ります。</p>
    <div class="more" style="margin-top:12px">READ MORE <svg width="34" height="8" viewBox="0 0 34 8"><polyline points="0,7 33,7 26,1" fill="none" stroke="#f29a2e" stroke-width="1.2"/></svg></div>
  </div>
  <div class="abs" style="left:496px;top:3150px;width:230px">
    <p class="body-text" style="font-size:12px">文章が入ります。文章が入ります。<br><br>文章が入ります。文章が入ります。<br>文章が入ります。文章が入ります。<br>文章が入ります。文章が入ります。</p>
    <div class="more" style="margin-top:12px">READ MORE <svg width="34" height="8" viewBox="0 0 34 8"><polyline points="0,7 33,7 26,1" fill="none" stroke="#f29a2e" stroke-width="1.2"/></svg></div>
  </div>
  <div class="abs" style="left:796px;top:3150px;width:230px">
    <p class="body-text" style="font-size:12px">文章が入ります。文章が入ります。<br><br>文章が入ります。文章が入ります。<br>文章が入ります。文章が入ります。<br>文章が入ります。文章が入ります。</p>
    <div class="more" style="margin-top:12px">READ MORE <svg width="34" height="8" viewBox="0 0 34 8"><polyline points="0,7 33,7 26,1" fill="none" stroke="#f29a2e" stroke-width="1.2"/></svg></div>
  </div>
</section>

<section class="news">
  <div class="band" style="left:0;top:3440px;width:1200px;height:400px"></div>
  <div class="card" style="left:152px;top:3528px;width:896px;height:212px"></div>
  <div class="abs" style="left:190px;top:3600px;width:150px">
    <div class="heading left" style="font-size:20px">NEWS<small>ニュース</small></div>
    <div class="more" style="margin-top:12px">READ MORE <svg width="34" height="8" viewBox="0 0 34 8"><polyline points="0,7 33,7 26,1" fill="none" stroke="#f29a2e" stroke-width="1.2"/></svg></div>
  </div>
  <div class="abs" style="left:356px;top:3562px;width:1px;height:150px;background:var(--line)"></div>
  <div class="abs" style="left:380px;top:3572px">
    <div class="news-row"><time>2017.07.01</time></div>
    <div class="news-row" style="margin-top:4px">タイトルが入ります。タイトルが入ります。タイトルが入ります。タイトルが入ります。</div>
    <div class="news-row" style="margin-top:22px"><time>2017.06.15</time></div>
    <div class="news-row" style="margin-top:4px">タイトルが入ります。タイトルが入ります。タイトルが入ります。タイトルが入ります。</div>
  </div>
</section>

<section class="contact">
  <div class="photo" role="img" aria-label="木々のある街並みの淡い背景写真" style="left:0;top:3840px;width:1200px;height:472px;background:linear-gradient(180deg,#eef0ea,#dfe3da 50%,#f2f2ef)"></div>
  <div class="abs" style="left:0;top:3910px;width:1200px">
    <div class="heading">CONTACT<small>サロン見学・お問い合わせはこちらから</small></div>
  </div>
  <div class="abs" style="left:330px;top:4056px;font-weight:700;font-size:30px;letter-spacing:.02em">LUMERA HAIR</div>
  <div class="abs" style="left:330px;top:4120px;display:flex;align-items:center;gap:8px;font-size:26px;font-weight:500">
    <svg width="22" height="24" viewBox="0 0 24 24"><path d="M6.6 10.8a15.1 15.1 0 006.6 6.6l2.2-2.2a1 1 0 011-.25 11.4 11.4 0 003.6.57 1 1 0 011 1V20a1 1 0 01-1 1A17 17 0 013 4a1 1 0 011-1h3.5a1 1 0 011 1 11.4 11.4 0 00.57 3.6 1 1 0 01-.25 1z" fill="#333"/></svg>
    045-612-3380
  </div>
  <div class="abs hours" style="left:330px;top:4170px">営業時間<br>平日：10:00～20:00<br>土曜：9:00～19:00<br>日祝：9:00～18:00</div>
  <div class="abs detail-btn" style="left:568px;top:4108px;width:320px;height:80px">詳しい情報はこちらから
    <svg width="34" height="8" viewBox="0 0 34 8"><polyline points="0,7 33,7 26,1" fill="none" stroke="#333" stroke-width="1.2"/></svg>
  </div>
  <svg class="abs" style="left:1130px;top:4226px" width="44" height="44" viewBox="0 0 44 44"><circle cx="22" cy="22" r="20" fill="#fff" stroke="#999"/><polyline points="15,25 22,18 29,25" fill="none" stroke="#666" stroke-width="1.5"/></svg>
</section>

<footer class="abs site-footer">
  <div class="social"><span></span><span></span><span></span><span></span></div>
  <nav class="foot-nav">
    <span>会社概要</span><span>当サロンについて</span><span>募集要項</span><span>教育システム</span><span>入社方法</span><span>サロン見学・お問い合わせ</span>
  </nav>
  <p class="copyright">Copyright © LUMERA HAIR. All Rights Reserved.</p>
</footer>

</body>
</html>
```